Business Card for TOV

We need a Corporate style business card for a new Industrial recycling company based in Australia. We recycle industrial products from Mining companies, power stations and other large industry all around the country.

We want the card to represent a modern, innovative professional company that is an industry leader.

We want the card to be double sided. I think with the logo centred by itself on one side and the text displayed with all our details on the other side.

(or you could put the persons name with the job title on the side with the logo?? I'll leave that up to your creative sides)

Open to how you divide and place the information on the one side of the card.

I think the persons name and the title should have its own place. The rest of the information can be placed as you think is best and then I will provide feedback as to what I think works best.

I have attached the logo file so you can add that to the one side. Whether you use it in a smaller form on the second side too is an option but I'll leave that up to you initially?

Information required on the card is as follows

Dermot Halloran
Director

0438 972 506

dermot@tovq.com.au

Po Box 782
Brindle ACT 2694

www.tovq.com.au

ACN 582 917 306 (This can be in very small print and can be in the bottom corner of the card or somewhere not very prominent

Wanted to thank everyone for their submissions. 

We were really torn on about 5 designs in the end.

We decided to go with the first one we liked.

We have another company that is going to need logo and business card design in the coming weeks.

I will save your designer ID's so I can invite you all to that project. too!

Thanks again and all the best

Dermot

Target Market(s)

Corporate and medium to large business clients

Industry/Entity Type

Industrial

```html
<!DOCTYPE html>
<html lang="en">
<head>
<meta charset="utf-8">
<title>TOV Business Card – Front and Back</title>
<link href="https://fonts.googleapis.com/css2?family=Arimo:wght@400;700&display=swap" rel="stylesheet">
<style>
  :root {
    --page: #ececec;
    --card: #ffffff;
    --band: #3f8db5;
    --band-light: #5aa3c7;
    --navy: #1c5a87;
    --ink: #3a3a3a;
    --brand: #2f7fae;
    --brand-dot: #5fb246;
    --white: #ffffff;
  }
  * { box-sizing: border-box; margin: 0; padding: 0; }
  html, body {
    width: 1200px; height: 900px; overflow: hidden;
    background: var(--page);
    font-family: "Arimo", Arial, sans-serif;
  }
  .canvas { position: relative; width: 1200px; height: 900px; }

  .card {
    position: absolute;
    width: 560px; height: 320px;
    background: var(--card);
    overflow: hidden;
    box-shadow: 0 6px 18px rgba(0,0,0,.18);
  }
  .card--front { left: 50px; top: 90px; }
  .card--back  { left: 590px; top: 490px; }

  .corner-block {
    position: absolute;
    background: linear-gradient(180deg, var(--navy), #2b6f9e);
  }

  .brand {
    position: absolute;
    display: flex; align-items: center; gap: 12px;
  }
  .brand__mark { border-radius: 50%; background: var(--brand-dot); flex: none; }
  .brand__name {
    font-weight: 700; color: var(--brand);
    text-transform: uppercase; line-height: 1.05; letter-spacing: .02em;
  }

  /* front */
  .card--front .brand { left: 34px; top: 44px; }
  .card--front .brand__mark { width: 64px; height: 64px; }
  .card--front .brand__name { font-size: 30px; }

  .contact-band {
    position: absolute; left: 300px; top: 128px; width: 260px; height: 84px;
    background: linear-gradient(90deg, var(--band), var(--band-light));
    padding: 10px 0 0 18px;
    color: var(--white); font-size: 13px;
  }
  .contact-list { list-style: none; display: flex; flex-direction: column; gap: 6px; }
  .contact-list li { display: flex; align-items: center; gap: 7px; white-space: nowrap; }
  .contact-list svg { width: 12px; height: 12px; flex: none; }

  .acn {
    position: absolute; right: 14px; top: 216px;
    font-size: 7px; color: var(--ink);
  }

  .person { position: absolute; left: 128px; top: 214px; }
  .person__name { font-size: 24px; font-weight: 700; color: var(--ink); letter-spacing: .01em; text-transform: uppercase; }
  .person__title { font-size: 13px; font-weight: 700; color: var(--ink); margin-left: 92px; }

  .card--front .corner-block { left: 60px; top: 262px; width: 58px; height: 58px; }

  /* back */
  .back-band {
    position: absolute; left: 330px; top: 80px; width: 230px; height: 120px;
    background: linear-gradient(90deg, var(--band), var(--band-light));
  }
  .website {
    position: absolute; left: 150px; top: 128px;
    font-size: 17px; color: var(--band); letter-spacing: .03em;
  }
  .card--back .brand { left: 120px; top: 236px; gap: 8px; }
  .card--back .brand__mark { width: 34px; height: 34px; }
  .card--back .brand__name { font-size: 15px; }
  .card--back .corner-block { left: 40px; top: 256px; width: 60px; height: 64px; }
</style>
</head>
<body>
<main class="canvas">

  <section class="card card--front" aria-label="Business card front">
    <div class="brand">
      <span class="brand__mark"></span>
      <span class="brand__name">Tovell Quarry<br>Reclaim</span>
    </div>

    <div class="contact-band">
      <ul class="contact-list">
        <li>
          <svg viewBox="0 0 12 12"><circle cx="6" cy="6" r="6" fill="#fff"/><path d="M4 3.2l1 1.4-.6.7c.4.9 1 1.5 1.9 1.9l.7-.6 1.4 1-.5 1.1C5.6 8.4 3.6 6.4 3.2 4.1z" fill="#3f8db5"/></svg>
          0438 972 506
        </li>
        <li>
          <svg viewBox="0 0 12 12"><circle cx="6" cy="6" r="6" fill="#fff"/><rect x="3" y="4" width="6" height="4.2" fill="none" stroke="#3f8db5" stroke-width=".9"/><path d="M3 4l3 2.3L9 4" fill="none" stroke="#3f8db5" stroke-width=".9"/></svg>
          dermot@tovq.com.au
        </li>
        <li>
          <svg viewBox="0 0 12 12"><circle cx="6" cy="6" r="6" fill="#fff"/><path d="M6 2.6a2.2 2.2 0 0 1 2.2 2.2C8.2 6.6 6 9.4 6 9.4S3.8 6.6 3.8 4.8A2.2 2.2 0 0 1 6 2.6z" fill="#3f8db5"/><circle cx="6" cy="4.8" r=".8" fill="#fff"/></svg>
          Po Box 782, Brindle ACT 2694
        </li>
      </ul>
    </div>
    <p class="acn">ACN 582 917 306</p>

    <div class="person">
      <p class="person__name">Dermot Halloran</p>
      <p class="person__title">Director</p>
    </div>

    <div class="corner-block"></div>
  </section>

  <section class="card card--back" aria-label="Business card back">
    <div class="back-band"></div>
    <p class="website">www.tovq.com.au</p>
    <div class="brand">
      <span class="brand__mark"></span>
      <span class="brand__name">Tovell Quarry<br>Reclaim</span>
    </div>
    <div class="corner-block"></div>
  </section>

</main>
</body>
</html>
```